NAT stands for Nell and Tova - teenager girls that will provide makeup and photography services for proms, weddings, graduations and other special events. The design should be bright and cheery and have the teenage audience it will be directed to in mind. I want the word "NAT" to be a part of the postcard and be essentially a logo by itself with the names somewhere under it.

Target Market(s)

Teenagers

Industry/Entity Type

Makeup

Requirements
Must have
• The Word "NAT" as the logo for the make up and photography services with the girls name in smaller font somewhere to identify what "NAT" stands for.
Nice to have
• I like circles and bright colors. I like tie dye too. There should be room to put a couple photos of their work on the postcard.
Should not have
• No address will be proved

```html
<!DOCTYPE html>
<html lang="en">
<head>
<meta charset="utf-8">
<title>NAT – Makeup &amp; Photography</title>
<link rel="stylesheet" href="https://fonts.googleapis.com/css2?family=Roboto+Slab:wght@400;700&family=Roboto:wght@400;700&display=swap">
<style>
  :root {
    --page: #ffffff;
    --hot-pink: #ee2a7b;
    --berry: #d8377f;
    --plum: #b04a8e;
    --lime: #e4f214;
    --sun: #ffe033;
    --ink: #111111;
    --blush: #f4b3cf;
    --dress-red: #e8262e;
    --hair-brown: #5a3424;
    --sky: #bcd9ee;
    --strip: #161616;
  }
  * { margin: 0; padding: 0; box-sizing: border-box; }
  html, body { width: 1200px; height: 930px; overflow: hidden; background: var(--page); }
  .postcard { position: relative; width: 1200px; height: 930px; background: var(--page); overflow: hidden; }

  .brand-band {
    position: absolute; left: 30px; top: 30px; width: 1140px; height: 235px;
    background: linear-gradient(90deg, var(--hot-pink) 0%, var(--berry) 60%, var(--plum) 100%);
  }
  .brand-rule { position: absolute; left: 30px; top: 265px; width: 1140px; height: 10px; background: var(--lime); }

  .brand-mark {
    position: absolute; left: 100px; top: 28px; width: 580px;
    font-family: "Roboto Slab", serif; font-weight: 700; font-size: 170px;
    line-height: 1; letter-spacing: 52px; color: var(--sun); white-space: nowrap;
  }
  .brand-names {
    position: absolute; left: 118px; top: 196px;
    font-family: "Roboto Slab", serif; font-weight: 400; font-size: 48px;
    letter-spacing: 4px; color: #ffffff; line-height: 1; white-space: nowrap;
  }

  .stage {
    position: absolute; left: 30px; top: 283px; width: 1140px; height: 495px;
    background: radial-gradient(ellipse 60% 55% at 40% 45%, #ffffff 0%, #fbeef4 45%, var(--blush) 100%);
    overflow: hidden;
  }
  .film-strip {
    position: absolute; left: 20px; top: -10px; width: 62px; height: 540px;
    background: var(--strip);
    transform: rotate(-11deg); transform-origin: top left;
  }

  .headline {
    position: absolute; left: 170px; top: 308px; width: 475px; text-align: center;
    font-family: "Roboto Slab", serif; font-weight: 700; font-size: 64px; line-height: 70px; color: var(--ink);
    white-space: nowrap;
  }
  .occasions {
    position: absolute; left: 170px; top: 452px; width: 475px; text-align: center;
    font-family: "Roboto", sans-serif; font-size: 24px; line-height: 36px; color: var(--ink);
    white-space: nowrap;
  }
  .credit {
    position: absolute; left: 270px; top: 580px; width: 355px; text-align: center;
    font-family: "Roboto", sans-serif; color: var(--ink);
  }
  .credit .by { font-size: 23px; line-height: 30px; }
  .credit .role { font-size: 22px; line-height: 28px; margin-top: 12px; }
  .credit .names { font-family: "Roboto Slab", serif; font-weight: 700; font-size: 37px; line-height: 44px; white-space: nowrap; }

  .feature-photo {
    position: absolute; left: 605px; top: 145px; width: 400px; height: 633px;
    background: linear-gradient(180deg, var(--hair-brown) 0%, #c98f74 28%, var(--dress-red) 50%, #c81e26 100%);
    border-radius: 190px 190px 30px 30px;
  }

  .work-photo {
    position: absolute; border-radius: 50%; border: 8px solid #ffffff;
    box-shadow: 0 2px 8px rgba(0,0,0,0.25);
  }
  .work-photo--friends { left: 888px; top: 53px; width: 266px; height: 266px;
    background: linear-gradient(160deg, #f07b3a 0%, #d9a68a 45%, #6e7fa8 100%); }
  .work-photo--sisters { left: 946px; top: 341px; width: 206px; height: 206px;
    background: linear-gradient(180deg, var(--sky) 0%, #c9a28a 50%, #3aa78a 100%); }
  .work-photo--portrait { left: 42px; top: 532px; width: 230px; height: 230px;
    background: linear-gradient(150deg, #a2693f 0%, #e6c1a6 50%, #7a8a55 100%); }

  .contact-bar { position: absolute; left: 30px; top: 785px; width: 1140px; height: 113px; background: var(--ink); }
  .contact {
    position: absolute; top: 818px; display: flex; align-items: center; gap: 16px;
    font-family: "Roboto", sans-serif; font-weight: 700; font-size: 34px; color: var(--sun); line-height: 1;
    white-space: nowrap;
  }
  .contact--phone { left: 88px; }
  .contact--email { left: 455px; }
</style>
</head>
<body>
<div class="postcard">
  <div class="brand-band"></div>
  <div class="brand-rule"></div>

  <div class="stage">
    <div class="film-strip" role="img" aria-label="Decorative strip of camera film running diagonally down the left edge"></div>
  </div>

  <div class="brand-mark">NAT</div>
  <div class="brand-names">Nell and Tova</div>

  <h1 class="headline">Makeup &amp;<br>Photography</h1>
  <p class="occasions">for prom, weddings, special dates,<br>dances or other special occasions</p>
  <div class="credit">
    <div class="by">BY</div>
    <div class="role">Teenagers</div>
    <div class="names">Nell and Tova</div>
  </div>

  <div class="feature-photo" role="img" aria-label="Photo of a teenage girl with long brown hair in a red strapless prom dress"></div>

  <div class="work-photo work-photo--friends" role="img" aria-label="Photo of smiling teenage friends giving thumbs up"></div>
  <div class="work-photo work-photo--sisters" role="img" aria-label="Photo of two laughing girls outdoors under a blue sky"></div>
  <div class="work-photo work-photo--portrait" role="img" aria-label="Portrait photo of a young woman looking upward"></div>

  <div class="contact-bar"></div>
  <div class="contact contact--phone">
    <svg width="48" height="48" viewBox="0 0 48 48" aria-hidden="true">
      <rect x="2" y="2" width="44" height="44" rx="7" fill="none" stroke="#ffe033" stroke-width="3"/>
      <path d="M17 11 h7 v7 h-4 v12 h4 v7 h-7 q-4 0 -4 -4 v-18 q0 -4 4 -4 z" fill="#ffe033"/>
    </svg>
    <span>555-014-2287</span>
  </div>
  <div class="contact contact--email">
    <svg width="56" height="36" viewBox="0 0 56 36" aria-hidden="true">
      <rect x="0" y="0" width="56" height="36" fill="#ffe033"/>
      <path d="M2 2 L28 22 L54 2" fill="none" stroke="#111" stroke-width="3"/>
      <path d="M2 34 L21 17 M54 34 L35 17" fill="none" stroke="#111" stroke-width="3"/>
    </svg>
    <span>NATmakeupandphoto@mailbox.com</span>
  </div>
</div>
</body>
</html>
```